Tallowbrook Fitness - Personal & Rehab Training

Business Card for my personal training business - Tallowbrook Fitness. I focus on personal and rehab training. I would like a double sided card, round edges. front of card will be my existing logo and the back will have an image (black and white or exercise, people exercising, weights, etc) along with my name and details. Such as:
Corisse Pembly
Personal & Rehab Trainer
www.tallowbrookfitness.com.au
0438264905
I have some images that I have downloaded that I am happy to send to the designer.
Thanks
Target Market(s)
athletes, middle to high income, sport related
Contact Information for Business Card
Corisse Pembly
Personal & Rehab Trainer
0438264905
Colors
Designer to choose only greyscale colors for use in the design.
Requirements
Must have
- my existing logo
Nice to have
- one of the images uploaded. I really like the girl with the mint coloured shoes as this is one of my logo colours

```html
<!DOCTYPE html>
<html lang="en">
<head>
<meta charset="utf-8">
<title>Tallowbrook Fitness – Business Card</title>
<link rel="stylesheet" href="https://fonts.googleapis.com/css2?family=Montserrat:wght@600;800&family=Roboto:wght@300;400;500&display=swap">
<style>
  :root {
    --page-bg: #2a2a2c;
    --card-black: #1b1b1d;
    --band-grey: #c8c9cc;
    --navy: #1e2a44;
    --white: #ffffff;
    --soft-white: #d9d9d9;
    --photo-dark: #2c2e33;
    --photo-mid: #55585e;
  }
  * { box-sizing: border-box; margin: 0; padding: 0; }
  html, body { width: 1200px; height: 1200px; overflow: hidden; }
  body {
    background: var(--page-bg);
    position: relative;
    font-family: "Roboto", Arial, sans-serif;
  }
  .card {
    position: absolute;
    width: 700px;
    height: 400px;
    border-radius: 26px;
    overflow: hidden;
    box-shadow: 0 18px 40px rgba(0,0,0,0.45);
  }
  .card-front { left: 110px; top: 120px; background: var(--band-grey); }
  .card-back { left: 390px; top: 660px; background: var(--card-black); }

  .front-photo {
    position: absolute;
    left: 0; top: 0;
    width: 100%; height: 280px;
    background: linear-gradient(160deg, var(--photo-mid) 0%, var(--photo-dark) 55%, #1f2024 100%);
  }
  .front-band {
    position: absolute;
    left: 0; top: 280px;
    width: 100%; height: 120px;
    display: flex; align-items: center; justify-content: center;
  }

  .brand {
    display: flex; align-items: center; gap: 18px;
  }
  .brand-square {
    border-radius: 10px;
    border-style: solid;
  }
  .brand-name {
    font-family: "Montserrat", Arial, sans-serif;
    font-weight: 600;
    text-transform: uppercase;
    letter-spacing: 0.14em;
  }
  .card-front .brand-square { width: 58px; height: 58px; border-width: 4px; border-color: var(--navy); }
  .card-front .brand-name { color: var(--navy); font-size: 28px; }

  .card-back .brand {
    position: absolute; left: 110px; top: 90px;
  }
  .card-back .brand-square { width: 88px; height: 88px; border-width: 5px; border-color: var(--white); border-radius: 14px; }
  .card-back .brand-name { color: var(--white); font-size: 36px; }

  .contact-row {
    position: absolute;
    left: 150px; bottom: 70px;
    display: flex; align-items: center; gap: 28px;
  }
  .person { text-align: right; }
  .person-name {
    font-family: "Montserrat", Arial, sans-serif;
    font-weight: 800;
    color: var(--white);
    font-size: 26px;
    letter-spacing: 0.02em;
    text-transform: uppercase;
  }
  .person-role {
    font-weight: 300;
    color: var(--soft-white);
    font-size: 17px;
    margin-top: 4px;
  }
  .divider { width: 1.5px; height: 70px; background: var(--soft-white); }
  .details { color: var(--white); font-size: 16px; font-weight: 500; line-height: 1.6; }
  .details .phone { font-size: 18px; }
</style>
</head>
<body>
  <section class="card card-front">
    <div class="front-photo" role="img" aria-label="Black and white gym photo of a woman in mint trainers gripping a kettlebell"></div>
    <div class="front-band">
      <div class="brand">
        <span class="brand-square"></span>
        <span class="brand-name">Tallowbrook Fitness</span>
      </div>
    </div>
  </section>

  <section class="card card-back">
    <div class="brand">
      <span class="brand-square"></span>
      <span class="brand-name">Tallowbrook Fitness</span>
    </div>
    <div class="contact-row">
      <div class="person">
        <p class="person-name">Corisse Pembly</p>
        <p class="person-role">Personal &amp; Rehab Trainer</p>
      </div>
      <span class="divider"></span>
      <div class="details">
        <p class="web">www.tallowbrookfitness.com.au</p>
        <p class="phone">0438264905</p>
      </div>
    </div>
  </section>
</body>
</html>
```